COOL PROJECT: Modern and Elegant Design for a Luxury Home Cleaning Company

We're looking for an elegant car wrap design for a Home Cleaning company based in Miami called The Halcyon Maids. We clean homes for medium to wealthy people and we want to attract this audience.

The design should communicate trust, professionalism & expertise. While looking SEXY!

Specs:
- Car Model: Voltara Series K Touring Edition 2020(I included a picture)
- Our Logo Font: Dosis Extra Bold(But if you have another cool font you want to test, we are open to other ideas)
- Please ensure to use the same colors as in the logo

Information to include on the car:
a. Slogan Options:
MORE THAN JUST A CLEANING
or
HALCYON GLOW, HIGH TO LOW

b. Our Website www.thehalcyonmaids.example

c. (305) 555 - 0148

d. I also included a few stamp design files, feel free to use these if you think it could look cool somewhere(Files: Stamp 1, stamp 2, stamp 3)

HAVE FUN!

```html
<!DOCTYPE html>
<html lang="en">
<head>
<meta charset="utf-8">
<title>The Halcyon Maids – Vehicle Wrap</title>
<link rel="stylesheet" href="https://fonts.googleapis.com/css2?family=Dosis:wght@600;700;800&display=swap">
<style>
  :root {
    --gold: #e3a92d;
    --navy: #1f3446;
    --white: #ffffff;
    --paper: #ffffff;
  }
  html, body {
    margin: 0;
    padding: 0;
    overflow: hidden;
    background: var(--paper);
  }
  .wrap-canvas {
    position: relative;
    width: 1200px;
    height: 1200px;
    overflow: hidden;
    background: var(--paper);
    font-family: "Dosis", sans-serif;
  }
  .wrap-shapes {
    position: absolute;
    inset: 0;
  }
  .brand-name {
    position: absolute;
    left: 238px;
    top: 500px;
    margin: 0;
    color: var(--navy);
    font-weight: 800;
    font-size: 64px;
    line-height: 0.95;
    letter-spacing: 0.5px;
    text-transform: uppercase;
  }
  .contact-line {
    position: absolute;
    left: 590px;
    top: 464px;
    margin: 0;
    color: var(--white);
    font-weight: 700;
    font-size: 27px;
    letter-spacing: 0.3px;
    white-space: nowrap;
  }
  .slogan {
    position: absolute;
    left: 572px;
    top: 530px;
    margin: 0;
    font-weight: 800;
    font-size: 42px;
    letter-spacing: 0.5px;
    white-space: nowrap;
  }
  .slogan-lead { color: var(--gold); }
  .slogan-tail { color: var(--navy); }
</style>
</head>
<body>
<main class="wrap-canvas">
  <svg class="wrap-shapes" width="1200" height="1200" viewBox="0 0 1200 1200" xmlns="http://www.w3.org/2000/svg">
    <!-- brand disc -->
    <circle class="brand-disc" cx="360" cy="600" r="250" fill="var(--gold)"/>
    <!-- brand mark square -->
    <rect class="brand-square" x="160" y="570" width="60" height="60" fill="var(--navy)"/>
    <!-- contact band -->
    <polygon class="contact-band" points="585,455 1150,440 1150,515 560,520" fill="var(--gold)"/>
    <!-- slogan strip -->
    <polygon class="slogan-strip" points="560,520 1150,515 1150,595 548,595" fill="var(--white)"/>
    <!-- service band -->
    <polygon class="service-band" points="548,595 1150,595 1150,668 530,668" fill="var(--navy)"/>
    <!-- service stamps -->
    <g class="service-stamps">
      <g role="img" aria-label="Service stamp: home cleaning">
        <circle cx="600" cy="631" r="27" fill="var(--gold)"/>
        <circle cx="600" cy="631" r="20" fill="none" stroke="var(--navy)" stroke-width="3"/>
      </g>
      <g role="img" aria-label="Service stamp: floor care">
        <circle cx="672" cy="631" r="27" fill="var(--gold)"/>
        <circle cx="672" cy="631" r="20" fill="none" stroke="var(--navy)" stroke-width="3"/>
      </g>
      <g role="img" aria-label="Service stamp: professional cleaner">
        <circle cx="744" cy="631" r="27" fill="var(--gold)"/>
        <circle cx="744" cy="631" r="20" fill="none" stroke="var(--navy)" stroke-width="3"/>
      </g>
    </g>
  </svg>

  <h1 class="brand-name">The<br>Halcyon<br>Maids</h1>

  <p class="contact-line">(305) 555 - 0148 | www.thehalcyonmaids.example</p>

  <p class="slogan"><span class="slogan-lead">HALCYON GLOW,</span> <span class="slogan-tail">HIGH TO LOW</span></p>
</main>
</body>
</html>
```